Stationary/Business Card for Maple Freight Hauling Company
Maple Freight
Professional
Dana R Whitcomb
Managing Partner
Maple Freight LLC
4172 Old Harbor Lane
Jacksonville, Fl 32299
dana@maplefreight-example.com
www.maplefreightlines-example.com
We are looking for stationary and business cards that can easily be printed in either black and white or color. We're open to any and all ideas. Also, just a heads up but the web address listed above is still a dummy site so it will be a bit useless for inspiration. Thank you in advance for all your hard work.

```html
<!DOCTYPE html>
<html lang="en">
<head>
<meta charset="utf-8">
<title>Maple Freight – Business Card</title>
<link rel="stylesheet" href="https://fonts.googleapis.com/css2?family=Open+Sans:wght@400;600;700;800&display=swap">
<style>
  :root {
    --page-bg: #eceae6;
    --card-white: #ffffff;
    --brand-green: #2f9a3c;
    --brand-green-light: #45b24f;
    --brand-green-dark: #23802f;
    --seam-grey: #c9c9c9;
    --text-light: #ffffff;
    --divider: rgba(255,255,255,0.75);
  }
  * { box-sizing: border-box; margin: 0; padding: 0; }
  html, body {
    width: 1200px; height: 780px; overflow: hidden;
    background: var(--page-bg);
    font-family: "Open Sans", Arial, sans-serif;
  }
  .canvas { position: relative; width: 1200px; height: 780px; }

  .business-card {
    position: absolute; left: 75px; top: 90px;
    width: 1050px; height: 600px;
    border-radius: 34px; overflow: hidden;
    background: var(--card-white);
    box-shadow: 0 10px 30px rgba(0,0,0,0.18);
  }

  .brand-area {
    position: absolute; left: 0; top: 0; width: 100%; height: 310px;
    display: flex; align-items: center; justify-content: center; gap: 22px;
    padding-top: 20px;
  }
  .brand-dot {
    width: 54px; height: 54px; border-radius: 50%;
    background: var(--brand-green);
  }
  .brand-name {
    font-family: "Open Sans", Arial, sans-serif;
    font-weight: 800; font-size: 78px; letter-spacing: -1px;
    color: var(--brand-green);
  }

  .contact-band {
    position: absolute; left: 0; top: 310px; width: 100%; height: 290px;
    background: linear-gradient(180deg, var(--brand-green-light) 0%, var(--brand-green) 45%, var(--brand-green-dark) 100%);
    border-top: 5px solid var(--seam-grey);
    color: var(--text-light);
  }

  .person-block {
    position: absolute; right: 570px; top: 50px;
    text-align: right; font-size: 25px; line-height: 38px; font-weight: 400;
  }
  .person-name { font-size: 31px; font-weight: 700; line-height: 44px; }

  .band-divider {
    position: absolute; left: 505px; top: 44px;
    width: 2px; height: 200px; background: var(--divider);
  }

  .contact-list {
    position: absolute; left: 525px; top: 44px;
    list-style: none; font-size: 23px; line-height: 40px;
  }
  .contact-list li { display: flex; align-items: center; gap: 12px; }
  .contact-list svg { width: 24px; height: 24px; flex: none; fill: var(--text-light); }
</style>
</head>
<body>
<div class="canvas">
  <article class="business-card">
    <header class="brand-area">
      <span class="brand-dot" aria-hidden="true"></span>
      <span class="brand-name">Maple Freight</span>
    </header>

    <section class="contact-band">
      <div class="person-block">
        <p class="person-name">Dana R Whitcomb</p>
        <p class="person-title">Managing Partner</p>
        <p class="company">Maple Freight LLC</p>
        <p class="street">4172 Old Harbor Lane</p>
        <p class="city">Jacksonville, Fl 32299</p>
      </div>

      <div class="band-divider"></div>

      <ul class="contact-list">
        <li>
          <svg viewBox="0 0 24 24" aria-label="phone"><path d="M6.6 10.8a15.1 15.1 0 0 0 6.6 6.6l2.2-2.2c.3-.3.7-.4 1-.2 1.1.4 2.3.6 3.6.6.6 0 1 .4 1 1V20c0 .6-.4 1-1 1C10.6 21 3 13.4 3 4c0-.6.4-1 1-1h3.5c.6 0 1 .4 1 1 0 1.3.2 2.5.6 3.6.1.3 0 .7-.2 1z"/></svg>
          <span>904-555-0162</span>
        </li>
        <li>
          <svg viewBox="0 0 24 24" aria-label="mobile"><path d="M7 2h10a1.5 1.5 0 0 1 1.5 1.5v17A1.5 1.5 0 0 1 17 22H7a1.5 1.5 0 0 1-1.5-1.5v-17A1.5 1.5 0 0 1 7 2zm0 3v12h10V5zm5 13.2a1 1 0 1 0 0 2 1 1 0 0 0 0-2z"/></svg>
          <span>904-555-0100</span>
        </li>
        <li>
          <svg viewBox="0 0 24 24" aria-label="fax"><path d="M6 2h9l3 3v5H6zM4 11h16a2 2 0 0 1 2 2v7a2 2 0 0 1-2 2H4a2 2 0 0 1-2-2v-7a2 2 0 0 1 2-2zm3 3v2h4v-2zm0 3v2h4v-2zm7-3v5h4v-5z"/></svg>
          <span>904-555-0164</span>
        </li>
        <li>
          <svg viewBox="0 0 24 24" aria-label="email"><path d="M3 5h18a1 1 0 0 1 1 1v12a1 1 0 0 1-1 1H3a1 1 0 0 1-1-1V6a1 1 0 0 1 1-1zm1 2.2V17h16V7.2l-8 5.3z M4.8 7 12 11.8 19.2 7z"/></svg>
          <span>dana@maplefreight-example.com</span>
        </li>
        <li>
          <svg viewBox="0 0 24 24" aria-label="website"><path d="M12 2a10 10 0 1 0 0 20 10 10 0 0 0 0-20zm6.9 9h-3a15 15 0 0 0-1.3-5.6A8 8 0 0 1 18.9 11zM12 4.1c.9 1.3 1.7 3.6 1.9 6.9h-3.8c.2-3.3 1-5.6 1.9-6.9zM9.4 5.4A15 15 0 0 0 8.1 11h-3a8 8 0 0 1 4.3-5.6zM5.1 13h3a15 15 0 0 0 1.3 5.6A8 8 0 0 1 5.1 13zm6.9 6.9c-.9-1.3-1.7-3.6-1.9-6.9h3.8c-.2 3.3-1 5.6-1.9 6.9zm2.6-1.3a15 15 0 0 0 1.3-5.6h3a8 8 0 0 1-4.3 5.6z"/></svg>
          <span>www.maplefreightlines-example.com</span>
        </li>
      </ul>
    </section>
  </article>
</div>
</body>
</html>
```